依頼詳細
PCとスマホデザインの両方納品をいただきますが、
まずはデザインイメージが確認しやすいPCページのみの提案をお願いします。
スマホページは当選者に納品時にお願いしたいと思います。
スマホサイズについて、表示は横幅375pxで作成し、
デザインデータは2倍の横幅750pxのカンバスサイズで作成してください。
(Retinaディスプレイに対応するため)
レスポンシブウェブデザインを意識したデザインでお願いします。

■サイトマップ
添付の画面遷移図をご確認ください。

■参考サイト
http://hoshizora-tetsuko.co.jp/

■内容について
鋳造部品等を製作する会社のサイトリニューアルになります。
既存サイト
http://www.senbeiseiko.com/kiyora/index.html

■素材写真
画像データについては、フリー素材から流用して
イメージ画像に当て込んでください。
足りない場合は、一旦他のサイトの写真をサンプルとして
入れてください。(サンプルなどの表記をお願いします)
また、購入が必要な写真などを利用した場合、
価格とサイト名を教えてください。

また、Lumera Photosで定期契約をしていますので、
Lumera Photosの画像は使用できます。
デザイン時はカンプ画像をお入れいただきますようお願いします。

■ワイヤーフレーム
https://mock.wirevista.net/view/1a2b3c4d-5e6f-4a7b-8c9d-0e1f2a3b4c5d-8812/?fullscreen
コンテンツの構成としてワイヤーフレームを作成しましたが
必ずしもワイヤーフレームの通りではなくて大丈夫です。
TOPページに配置するコンテンツを見ていただき、デザインは
デザイナーの皆様におまかせしたいと思います。

----------------------------------------------------------------------------
【制作物に対するお願い】

■フォントについて
・無料で使えるフォントで作成をお願いします。
・OSに紐づくフォントの使用は控えていただければと思います (ヒラギノなど)

ページ数
1ページ
希望イメージ
シンプル 複雑
単色 カラフル
暗い 明るい
日常 高級
遊び心 厳粛
未来的 伝統的
女性的 男性的
希望する色
アクセントカラー:茶色、もしくは青色
納品ファイル
• 高解像度JPG (.jpg)
• イラストレーター形式 (.ai)
• フォトショップ形式 (.psd)
補足説明
上記のいずれか1つ(アウトラインありとなしの2つ)と高解像度JPGを納品お願いします。
adobe XDでの納品も可能です。

```html
<!DOCTYPE html>
<html lang="ja">
<head>
<meta charset="utf-8">
<title>丸栄メタル工業株式会社</title>
<link rel="stylesheet" href="https://fonts.googleapis.com/css2?family=Noto+Sans+JP:wght@400;500;700&family=Montserrat:wght@500;700&display=swap">
<style>
:root{
  --brown:#6e4126;
  --brown-dark:#3b2418;
  --accent:#c0703e;
  --accent-soft:#d99a70;
  --pale:#f7ebe5;
  --peach:#efc3a8;
  --gray-bg:#f1eeec;
  --text:#3a302b;
  --muted:#7a706a;
  --white:#ffffff;
}
*{margin:0;padding:0;box-sizing:border-box}
html,body{width:1200px;height:4380px;overflow:hidden}
body{font-family:"Noto Sans JP",sans-serif;color:var(--text);background:var(--white);position:relative}
.abs{position:absolute}
.btn{display:inline-flex;align-items:center;justify-content:center;gap:10px;background:var(--accent);color:var(--white);font-family:"Montserrat",sans-serif;font-size:12px;font-weight:700;letter-spacing:.08em;width:200px;height:40px}
.btn::after{content:"";width:30px;height:1px;background:var(--white)}
.sec-title{font-size:30px;font-weight:700;letter-spacing:.1em;text-align:center}
.sec-title::after{content:"";display:block;width:40px;height:2px;background:var(--accent);margin:14px auto 0}
.body-text{font-size:14px;line-height:2;color:var(--muted)}

/* header / hero */
.hero{top:0;left:0;width:1200px;height:680px;background:radial-gradient(ellipse at 62% 62%,#f08a3a 0%,#b8542a 18%,#5e2f1c 45%,#2e1a12 80%)}
.logo-box{top:28px;left:70px;width:110px;height:40px;border:1px solid var(--white);color:var(--white);font-size:13px;display:flex;align-items:center;justify-content:center;background:rgba(255,255,255,.1)}
.nav{top:44px;left:700px;display:flex;gap:40px;color:var(--white);font-size:13px}
.nav-contact{top:28px;left:1060px;width:110px;height:42px;background:var(--accent);color:var(--white);font-size:12px;display:flex;align-items:center;justify-content:center}
.hero-title{top:180px;left:110px;color:var(--white)}
.hero-title h1{font-size:46px;font-weight:700;letter-spacing:.08em}
.hero-title .en{font-family:"Montserrat",sans-serif;font-size:30px;font-weight:700;letter-spacing:.12em;margin-top:8px}
.hero-title .tag{font-size:18px;margin-top:34px;letter-spacing:.1em}

/* about */
.about-bg{top:680px;left:0;width:860px;height:780px;background:var(--pale)}
.about-title{top:760px;left:0;width:1200px}
.about-lead{top:880px;left:130px;width:400px;font-size:20px;font-weight:700;line-height:1.7}
.about-text{top:980px;left:130px;width:410px}
.about-btn{top:1180px;left:130px}
.about-photo{top:890px;left:600px;width:520px;height:300px;background:linear-gradient(135deg,#8a8580,#4a3a30 55%,#d8743a 80%,#3a2e28)}

/* products */
.prod-title{top:1570px;left:0;width:1200px}
.cards{top:1680px;left:85px;display:flex;gap:45px}
.card{width:320px;height:490px;background:var(--white);box-shadow:0 4px 18px rgba(0,0,0,.1)}
.card .ph{height:240px}
.card h3{font-size:16px;font-weight:700;text-align:center;color:var(--accent);margin:34px 0 18px}
.card p{font-size:12px;line-height:1.9;color:var(--muted);padding:0 30px}
.ph-a{background:linear-gradient(135deg,#6f7780,#c9ced4,#4d5660)}
.ph-b{background:linear-gradient(135deg,#f3f5f7,#c9d0d8,#e9ecef)}
.ph-c{background:linear-gradient(135deg,#9aa3ad,#dfe3e7,#6d7782)}

/* manufacturing */
.mfg-shadow{top:2380px;left:30px;width:630px;height:460px;background:var(--peach)}
.mfg-photo{top:2350px;left:0;width:630px;height:460px;background:linear-gradient(160deg,#5e6a75,#2c3138 60%,#c58a4a 85%,#262a30)}
.mfg-title{top:2350px;left:750px;font-size:30px;font-weight:700;letter-spacing:.1em}
.mfg-lead{top:2420px;left:750px;width:400px;font-size:20px;font-weight:700;line-height:1.7}
.mfg-text{top:2530px;left:750px;width:400px}
.mfg-btn{top:2680px;left:750px}

/* recruit */
.recruit{top:2940px;left:0;width:1200px;height:400px;background:linear-gradient(100deg,#2a1e18,#5a3a28 50%,#2e2019)}
.recruit-inner{top:2985px;left:0;width:1200px;text-align:center;color:var(--white)}
.recruit-inner h2{font-size:30px;font-weight:700;letter-spacing:.1em;text-align:right;padding-right:440px}
.recruit-inner .lead{font-size:20px;font-weight:700;margin-top:24px}
.recruit-inner p{font-size:13px;line-height:2;margin:18px auto 0;width:560px;opacity:.9}
.recruit-btn{top:3270px;left:480px;width:240px}

/* news */
.news{top:3380px;left:0;width:1200px;height:420px;background:var(--gray-bg)}
.news-title{top:3480px;left:80px;font-size:26px;font-weight:700;letter-spacing:.1em}
.news-all{top:3540px;left:80px;width:90px;height:32px;border:1px solid var(--accent);color:var(--accent);font-size:12px;display:flex;align-items:center;justify-content:center}
.news-list{top:3470px;left:360px;width:440px;list-style:none}
.news-list li{border-bottom:1px solid #ddd6d1;padding:12px 0 14px}
.news-list time{display:block;font-family:"Montserrat",sans-serif;font-size:11px;color:var(--muted)}
.news-list span{font-size:12px;color:var(--text);display:block;margin-top:8px}

/* contact */
.contact-lead{top:3900px;left:0;width:1200px;text-align:center;font-size:16px;letter-spacing:.05em}
.tel-box{top:3970px;left:280px;width:300px;height:120px;border:2px solid var(--accent-soft);text-align:center;padding-top:30px}
.tel-box strong{font-size:30px;color:var(--accent);font-weight:700}
.tel-box small{display:block;font-size:11px;color:var(--muted);margin-top:4px}
.mail-box{top:3970px;left:620px;width:300px;height:120px;background:linear-gradient(90deg,#b8683a,#d08a5c);color:var(--white);font-size:20px;font-weight:700;display:flex;align-items:center;justify-content:center}

/* footer */
.footer{top:4160px;left:0;width:1200px;height:220px;background:var(--brown)}
.foot-links{top:4210px;left:80px;display:grid;grid-template-columns:repeat(6,auto);gap:14px 30px;color:var(--white);font-size:12px}
.foot-logo{top:4210px;left:990px;width:110px;height:40px;border:1px solid var(--white);background:rgba(255,255,255,.1);color:var(--white);font-size:13px;display:flex;align-items:center;justify-content:center}
.copy{top:4340px;left:0;width:1120px;text-align:right;color:rgba(255,255,255,.75);font-size:10px}
</style>
</head>
<body>

<div class="abs hero" role="img" aria-label="鍛冶場で赤く熱した金属を打つ写真"></div>
<div class="abs logo-box">丸栄メタル</div>
<nav class="abs nav"><span>会社案内</span><span>製造案内</span><span>製品紹介</span><span>採用情報</span></nav>
<div class="abs nav-contact">お問い合わせ</div>
<div class="abs hero-title">
  <h1>丸栄メタル工業株式会社</h1>
  <div class="en">MARUEI METAL</div>
  <p class="tag">製造技術に、自信と誇りを持って</p>
</div>

<div class="abs about-bg"></div>
<h2 class="abs about-title sec-title">丸栄メタルとは</h2>
<p class="abs about-lead">モノ造りのプロとして確かな技術で<br>お応えします。</p>
<p class="abs about-text body-text">丸栄メタル工業株式会社は創業以来、銅合金の鋳造部品を専門に製作してまいりました。長年培った技術と経験を活かし、お客様のご要望に合わせた製品を一つひとつ丁寧にお届けしています。品質と納期を大切にするものづくりを続けます。</p>
<div class="abs about-btn btn">READ MORE</div>
<div class="abs about-photo" role="img" aria-label="金床で熱した鉄を打つ職人の手元の写真"></div>

<h2 class="abs prod-title sec-title">製品紹介</h2>
<div class="abs cards">
  <div class="card"><div class="ph ph-a" role="img" aria-label="機械部品の写真"></div><h3>機械部品</h3><p>テキストが入ります。テキストが入ります。テキストが入ります。テキストが入ります。テキストが入ります。</p></div>
  <div class="card"><div class="ph ph-b" role="img" aria-label="電子部品の写真"></div><h3>電子部品</h3><p>テキストが入ります。テキストが入ります。テキストが入ります。テキストが入ります。テキストが入ります。</p></div>
  <div class="card"><div class="ph ph-c" role="img" aria-label="ボルトなど金属部品の写真"></div><h3>その他の部品</h3><p>テキストが入ります。テキストが入ります。テキストが入ります。テキストが入ります。テキストが入ります。</p></div>
</div>

<div class="abs mfg-shadow"></div>
<div class="abs mfg-photo" role="img" aria-label="工場で溶接作業をする様子の写真"></div>
<h2 class="abs mfg-title">製造案内</h2>
<p class="abs mfg-lead">充実した設備と確かな技術でお客様のご要望に応えます</p>
<p class="abs mfg-text body-text">丸栄メタル工業株式会社では、充実した設備と熟練の技術者により、小ロットから量産まで幅広く対応いたします。お客様のご要望に応じた最適な製品をご提案します。</p>
<div class="abs mfg-btn btn">READ MORE</div>

<div class="abs recruit" role="img" aria-label="作業場で働く職人の写真"></div>
<div class="abs recruit-inner">
  <h2>採用情報</h2>
  <p class="lead">丸栄メタルではともに働く仲間を募集しています。</p>
  <p>丸栄メタル工業株式会社では、ものづくりに情熱を持つ方を募集しています。未経験の方も丁寧に指導いたしますので、安心してご応募ください。皆様のご応募をお待ちしております。</p>
</div>
<div class="abs recruit-btn btn">READ MORE</div>

<div class="abs news"></div>
<h2 class="abs news-title">お知らせ</h2>
<div class="abs news-all">一覧 →</div>
<ul class="abs news-list">
  <li><time>2020.00.00</time><span>テキストが入ります。テキストが入ります。テキストが入ります。</span></li>
  <li><time>2020.00.00</time><span>テキストが入ります。テキストが入ります。テキストが入ります。</span></li>
  <li><time>2020.00.00</time><span>テキストが入ります。テキストが入ります。テキストが入ります。</span></li>
</ul>

<p class="abs contact-lead">質問やご相談を承ります。どうぞ、お気軽にお問い合わせください。</p>
<div class="abs tel-box"><strong>TEL:03-0000-1234</strong><small>受付時間 平日9:00〜17:00</small></div>
<div class="abs mail-box">メールでのお問い合わせ</div>

<footer class="abs footer"></footer>
<div class="abs foot-links">
  <span>トップページ</span><span>会社案内</span><span>製造案内</span><span>製品紹介</span><span>採用情報</span><span></span>
  <span>お知らせ</span><span>お問い合わせ</span><span>プライバシーポリシー</span><span>サイトマップ</span><span></span><span></span>
</div>
<div class="abs foot-logo">丸栄メタル</div>
<p class="abs copy">Copyright © Maruei Metal Co., Ltd. All Rights Reserved.</p>

</body>
</html>
```